Computer Service Provider in Need of New Letterhead Design

We are Larkvale Computer Services, a computer/IT services company that provides IT Support, software, hardware, virus monitoring, etc. in Vermont. We are looking for new letterhead, that is both professional and matches the current theme of our business cards & website.
Please note that we want to include the following information:
www.Larkvale.example
802-555-0147
47 Fernwick Hollow Road, Marlow Falls, VT 05999
Proactive Solutions • Approachable People • Proven Performance
I will be attaching our logo along with the business card images.
We would love to have the

```html
<!DOCTYPE html>
<html lang="en">
<head>
<meta charset="utf-8">
<title>Larkvale Computer Services — Letterhead</title>
<link href="https://fonts.googleapis.com/css2?family=Source+Sans+3:wght@400;600;700&family=Open+Sans:wght@400&display=swap" rel="stylesheet">
<style>
  :root {
    --brand-blue: #2a5885;
    --body-text: #575757;
    --rule: #3a3a3a;
    --footer-text: #444444;
    --paper: #ffffff;
    --signature-tone: #e4e4e4;
  }
  html, body {
    margin: 0;
    padding: 0;
    width: 943px;
    height: 1200px;
    overflow: hidden;
    background: var(--paper);
  }
  .letterhead {
    position: relative;
    width: 943px;
    height: 1200px;
    background: var(--paper);
    font-family: "Source Sans 3", "Myriad Pro", sans-serif;
  }
  .brand {
    position: absolute;
    top: 91px;
    left: 0;
    width: 943px;
    display: flex;
    justify-content: center;
    align-items: center;
    gap: 16px;
  }
  .brand-square {
    width: 64px;
    height: 64px;
    background: var(--brand-blue);
  }
  .brand-name {
    font-weight: 600;
    font-size: 30px;
    color: var(--brand-blue);
    letter-spacing: 0.2px;
  }
  .rule {
    position: absolute;
    height: 0;
    border-top: 1.3px solid var(--rule);
  }
  .rule-top { top: 204px; left: 64px; width: 817px; }
  .rule-bottom { top: 1072px; left: 54px; width: 832px; }
  .letter-body {
    position: absolute;
    top: 235px;
    left: 65px;
    width: 826px;
    color: var(--body-text);
    font-size: 18px;
    letter-spacing: 0.3px;
    line-height: 21.8px;
  }
  .letter-body p {
    margin: 0 0 21.8px;
    text-align: justify;
  }
  .signature {
    position: absolute;
    top: 972px;
    left: 680px;
    width: 168px;
    height: 30px;
    background: linear-gradient(90deg, var(--signature-tone), #f2f2f2);
    border-radius: 4px;
  }
  .signer-name {
    position: absolute;
    top: 1010px;
    left: 707px;
    width: 130px;
    text-align: center;
    color: var(--body-text);
    font-size: 17.5px;
    letter-spacing: 0.3px;
  }
  .contact-address {
    position: absolute;
    top: 1091px;
    left: 0;
    width: 943px;
    text-align: center;
    font-family: "Open Sans", sans-serif;
    font-size: 12.2px;
    letter-spacing: 1px;
    color: var(--footer-text);
  }
  .contact-lines {
    position: absolute;
    top: 1122px;
    left: 0;
    width: 943px;
    display: flex;
    justify-content: center;
    gap: 20px;
    font-family: "Open Sans", sans-serif;
    font-size: 12.2px;
    letter-spacing: 0.9px;
    color: var(--footer-text);
  }
  .contact-item {
    display: flex;
    align-items: center;
    gap: 8px;
  }
  .contact-icon {
    width: 11px;
    height: 11px;
    fill: var(--brand-blue);
  }
</style>
</head>
<body>
<main class="letterhead">
  <header class="brand">
    <div class="brand-square"></div>
    <div class="brand-name">Larkvale Computer Services</div>
  </header>

  <div class="rule rule-top"></div>

  <section class="letter-body">
    <p>Lorem ipsum dolor sit amet, consectetur adipiscing elit, sed do eiusmod tempor incididunt ut labore et dolore magna aliqua. Ut enim ad minim veniam, quis nostrud exercitation ullamco laboris nisi ut aliquip ex ea commodo consequat. Duis aute irure dolor in reprehenderit in voluptate velit esse cillum dolore eu fugiat nulla pariatur. Excepteur sint occaecat cupidatat non proident, sunt in culpa qui officia deserunt mollit anim id est laborum</p>
    <p>Sed ut perspiciatis unde omnis iste natus error sit voluptatem accusantium doloremque laudantium, totam rem aperiam, eaque ipsa quae ab illo inventore veritatis et quasi architecto beatae vitae dicta sunt explicabo. Nemo enim ipsam voluptatem quia voluptas sit aspernatur aut odit aut fugit, sed quia consequuntur magni dolores eos qui ratione voluptatem sequi nesciunt. Neque porro quisquam est, qui dolorem ipsum quia dolor sit amet, consectetur, adipisci velit, sed quia non numquam eius modi tempora incidunt ut labore et dolore magnam aliquam quaerat voluptatem. Ut enim ad minima veniam, quis nostrum exercitationem ullam corporis suscipit laboriosam, nisi ut aliquid ex ea commodi consequatur? Quis autem vel eum iure reprehenderit qui in ea voluptate velit esse quam nihil molestiae consequatur, vel illum qui dolorem eum fugiat quo voluptas nulla pariatur?</p>
    <p>Lorem ipsum dolor sit amet, consectetur adipiscing elit, sed do eiusmod tempor incididunt ut labore et dolore magna aliqua. Ut enim ad minim veniam, quis nostrud exercitation ullamco laboris nisi ut aliquip ex ea commodo consequat. Duis aute irure dolor in reprehenderit in voluptate velit esse cillum dolore eu fugiat nulla pariatur. Excepteur sint occaecat cupidatat non proident, sunt in culpa qui officia deserunt mollit anim id est laborum</p>
    <p>Sed ut perspiciatis unde omnis iste natus error sit voluptatem accusantium doloremque laudantium, totam rem aperiam, eaque ipsa quae ab illo inventore veritatis et quasi architecto beatae vitae dicta sunt explicabo. Nemo enim ipsam voluptatem quia voluptas sit aspernatur aut odit aut fugit, sed quia consequuntur magni dolores eos qui ratione voluptatem sequi nesciunt. Neque porro quisquam est, qui dolorem ipsum quia dolor sit amet, consectetur, adipisci velit, sed quia non numquam eius modi tempora incidunt ut labore et dolore magnam aliquam quaerat voluptatem. Ut enim ad minima veniam, quis nostrum exercitationem ullam corporis suscipit laboriosam, nisi ut aliquid ex ea commodi consequatur? Quis autem vel eum iure reprehenderit qui in ea voluptate velit esse quam nihil molestiae consequatur, vel illum qui dolorem eum fugiat quo voluptas nulla pariatur?</p>
  </section>

  <div class="signature" role="img" aria-label="Handwritten signature"></div>
  <div class="signer-name">Name Name</div>

  <div class="rule rule-bottom"></div>

  <footer>
    <div class="contact-address">47 Fernwick Hollow Road, Marlow Falls, VT 05999</div>
    <div class="contact-lines">
      <span class="contact-item">
        <svg class="contact-icon" viewBox="0 0 24 24" aria-hidden="true"><path d="M6.6 10.8a15.1 15.1 0 0 0 6.6 6.6l2.2-2.2a1 1 0 0 1 1-.25 11.4 11.4 0 0 0 3.6.57 1 1 0 0 1 1 1V20a1 1 0 0 1-1 1A17 17 0 0 1 3 4a1 1 0 0 1 1-1h3.5a1 1 0 0 1 1 1c0 1.250.2 2.45.57 3.57a1 1 0 0 1-.25 1z"/></svg>
        802-555-0147
      </span>
      <span class="contact-item">
        <svg class="contact-icon" viewBox="0 0 24 24" aria-hidden="true"><path d="M2 5h20v2l-10 6L2 7z"/><path d="M2 9l10 6 10-6v10H2z"/></svg>
        info@Larkvale.example
      </span>
      <span class="contact-item">
        <svg class="contact-icon" viewBox="0 0 24 24" aria-hidden="true"><circle cx="12" cy="12" r="10"/><path d="M2 12h20M12 2c3 3 3 17 0 20M12 2c-3 3-3 17 0 20" stroke="#fff" stroke-width="1.5" fill="none"/></svg>
        www.Larkvale.example
      </span>
    </div>
  </footer>
</main>
</body>
</html>
```